Email Template for AI Website Builder Marketing Campaign

Update: All the designs submitted have too much content for an email template. I have attached a mockup example of a simplified design. Please follow this guideline to revise your design to be less "wordy" and have less content to optimize the delivery rate of the emails. I have also attached the images I used to create the mockup. Feel free to use these images for your revised designs.
Original Brief:
I need a catchy email template for my new AI Website Builder, WebQuilt.ai. The template must be professional, colorful, yet not too complex. The concept of the product is this:
WebQuilt uses Artificial Intelligence (AI) to instantly build stunning websites, absolutely FREE. The user simply specifies their business name and business category (industry), and their stunning new website appears before their eyes!
The template will be used in MailChimp, so please provide the code that I can simply paste into the email body.
Here is a screenshot of our new website (which is not online yet) so you can match the color scheme and style of the email template to the new website design:
https://pixbinstore.com/art_img/7310582/2208634/48165027/9qrt41hwk826zlmpb3nqd7wyex_image.jpg
Let me know if you have any questions.
Thanks!
All submitted designs are too lengthy (too much content) for an email template. I will provide a mockup showing a sample of how you can simplify your design to function better as an email template and better suit my needs. I appreciate your patience!

```html
<!DOCTYPE html>
<html lang="en">
<head>
<meta charset="utf-8">
<title>WebQuilt – Your Free AI Website</title>
<link href="https://fonts.googleapis.com/css2?family=Roboto:wght@400;500;700;900&display=swap" rel="stylesheet">
<style>
  :root {
    --navy: #0b1f3d;
    --navy-deep: #07162e;
    --hero-top: #0c2550;
    --cyan: #3ec8f5;
    --blue: #2e8bf0;
    --blue-light: #5fb3ff;
    --orange: #ff8a1e;
    --orange-deep: #f2620a;
    --ink: #0e1b33;
    --grey: #666c74;
    --grey-soft: #8a8f96;
    --white: #ffffff;
  }
  * { margin: 0; padding: 0; box-sizing: border-box; }
  html, body { width: 1200px; height: 2576px; overflow: hidden; background: var(--white); }
  body { position: relative; font-family: "Roboto", Arial, sans-serif; color: var(--ink); }

  .browser-link {
    position: absolute; top: 36px; left: 0; width: 1200px; text-align: center;
    font-size: 25px; line-height: 32px; color: var(--grey);
  }

  .hero {
    position: absolute; top: 100px; left: 0; width: 1200px; height: 900px;
    background: radial-gradient(ellipse at 75% 35%, #1d5aa8 0%, var(--hero-top) 45%, var(--navy-deep) 100%);
    overflow: hidden;
  }
  .hero-art {
    position: absolute; left: 480px; top: 40px; width: 720px; height: 720px;
    background: radial-gradient(ellipse at 50% 45%, rgba(120,200,255,0.55) 0%, rgba(40,120,220,0.35) 40%, rgba(12,37,80,0) 72%);
  }
  .hero-skyline {
    position: absolute; left: 0; top: 560px; width: 620px; height: 240px;
    background: linear-gradient(180deg, rgba(20,50,100,0) 0%, rgba(35,80,140,0.45) 100%);
  }
  .brand-mark {
    position: absolute; width: 84px; height: 84px; border-radius: 50%; background: var(--cyan);
  }
  .brand {
    position: absolute; font-weight: 700; color: var(--white); letter-spacing: 0.5px;
    font-size: 64px; line-height: 76px; white-space: nowrap;
  }
  .hero .brand-mark { left: 62px; top: 92px; }
  .hero .brand { left: 168px; top: 96px; }
  .hero-title {
    position: absolute; left: 18px; top: 351px; width: 640px; text-align: center;
    font-size: 52px; font-weight: 700; line-height: 62px; color: var(--white); white-space: nowrap;
  }
  .hero-title .accent { color: var(--cyan); font-weight: 900; }
  .btn-hero {
    position: absolute; left: 92px; top: 588px; width: 492px; height: 88px; border-radius: 44px;
    background: linear-gradient(180deg, #ffa030 0%, var(--orange-deep) 100%);
    color: var(--ink); font-size: 29px; font-weight: 500; letter-spacing: 0.3px;
    display: flex; align-items: center; justify-content: center;
  }
  .hero-wave { position: absolute; left: 0; top: 700px; width: 1200px; height: 200px; }

  .welcome-kicker { position: absolute; left: 46px; top: 1056px; font-size: 30px; line-height: 36px; font-weight: 500; color: var(--blue); }
  .welcome-name { position: absolute; left: 44px; top: 1094px; font-size: 72px; font-weight: 700; color: var(--ink); line-height: 80px; }
  .welcome-lead { position: absolute; left: 46px; top: 1192px; font-size: 34px; font-weight: 700; line-height: 52px; color: var(--ink); white-space: nowrap; }
  .welcome-body { position: absolute; left: 46px; top: 1402px; font-size: 30px; line-height: 48px; color: var(--grey); white-space: nowrap; }

  .devices-art {
    position: absolute; left: 648px; top: 1134px; width: 492px; height: 432px; border-radius: 10px;
    background: linear-gradient(160deg, #e9eef4 0%, #c6d3e2 45%, #8fa5bd 100%);
  }

  .btn-primary {
    position: absolute; left: 146px; top: 1848px; width: 909px; height: 115px; border-radius: 58px;
    background: linear-gradient(180deg, #8cc8ff 0%, var(--blue) 45%, #1a72e6 100%);
    color: var(--white); font-size: 49px; font-weight: 700;
    display: flex; align-items: center; justify-content: center;
  }

  .footer-stripe { position: absolute; left: 0; top: 2040px; width: 1200px; height: 14px; background: var(--blue); }
  .footer {
    position: absolute; left: 0; top: 2054px; width: 1200px; height: 300px; background: var(--navy);
  }
  .footer .brand-mark { left: 76px; top: 112px; }
  .footer .brand { left: 182px; top: 116px; }
  .btn-footer {
    position: absolute; left: 652px; top: 102px; width: 496px; height: 100px; border-radius: 50px;
    background: linear-gradient(180deg, #ff9a2a 0%, var(--orange-deep) 100%);
    color: var(--white); font-size: 34px; font-weight: 700;
    display: flex; align-items: center; justify-content: center;
  }

  .legal { position: absolute; left: 0; top: 2428px; width: 1200px; text-align: center; font-size: 26px; color: var(--grey-soft); line-height: 37px; }
  .legal .unsubscribe { text-decoration: underline; color: var(--grey-soft); }
</style>
</head>
<body>
  <div class="browser-link">view in web browser</div>

  <section class="hero">
    <div class="hero-skyline" role="img" aria-label="Blurred night city skyline"></div>
    <div class="hero-art" role="img" aria-label="Glowing AI brain network above a robotic hand"></div>
    <div class="brand-mark" aria-hidden="true"></div>
    <div class="brand">WebQuilt</div>
    <h1 class="hero-title">Your <span class="accent">FREE</span> Stunning<br>Website in <span class="accent">1-Click</span> Built<br>By <span class="accent">Artificial Intelligence</span></h1>
    <div class="btn-hero">BUILD MY FREE WEBSITE</div>
    <svg class="hero-wave" viewBox="0 0 1200 200" preserveAspectRatio="none" aria-hidden="true">
      <path d="M0 40 C120 60 200 100 300 90 C600 60 900 10 1200 0 L1200 4 C900 20 500 120 260 184 C150 200 60 170 0 136 Z" fill="#2e8bf0"/>
      <path d="M0 136 C60 170 150 200 260 184 C500 120 900 20 1200 4 L1200 200 L0 200 Z" fill="#ffffff"/>
    </svg>
  </section>

  <div class="welcome-kicker">welcome to</div>
  <h2 class="welcome-name">WebQuilt</h2>
  <p class="welcome-lead">Harness the Power of Artificial<br>Intelligence to Instantly Build Your<br>Amazing FREE Website Today!</p>
  <p class="welcome-body">WebQuilt is the World’s first website<br>build that builds professional,<br>high-quality websites in seconds! Say<br>gooodbye to the traditional expensive<br>and time-consuming methods of<br>getting your business Online!</p>

  <div class="devices-art" role="img" aria-label="Website shown on desktop monitor, tablet and phone"></div>

  <div class="btn-primary">Generate FREE Website Now</div>

  <div class="footer-stripe"></div>
  <footer class="footer">
    <div class="brand-mark" aria-hidden="true"></div>
    <div class="brand">WebQuilt</div>
    <div class="btn-footer">Get Your FREE Website</div>
  </footer>

  <div class="legal">
    4820 Harbor Lane, Milford DE 19963<br>
    <span class="unsubscribe">Unsubscribe</span>
  </div>
</body>
</html>
```